Brazilian wine business need a label for a sparkling wine

We are importing a new italian sparkling wine, but we need to build our own brand. Our main focus is to sell sparkling wine for events, specially for weddings. So, specially for this audience, presentation is key.
We like to see wine in a "uncomplicated" way.
It is a mid price product.
The foil capsule color must be black, white or silver, due to production restrictions. We cannot have any graphic interference in this part, also.

We need to develop a label for it. The name will be "Lucenti Brut" (means "hug" in italian).

Our main public is people around the early 30s, so it should look modern and clean.
It is good, but not mandatory, to have a few information at the front label:
- Alcohol % (12%)
- Origin (Italy)

We need to avoid a few colours, for different reasons:
- Don´t use yellow/orange: too linked to Maison Dorvalle;
- Don´t use red or pink: people think it is a rosé, but it is a white.
Our idea is to work with white and blue or turquoise, maybe a green, something like that. Can have a touch of gold, also. (more references in the color tab below)
- The bottle is black.

Industry/Entity Type

Business

Font styles to use
Other font styles liked:
• Berlin Sans FB Regular or something less "round" but similar to Cooper Black Regular

Colors
00a990
33b8a4

Requirements
Must have
• As the name means "hug", we want to have a graphic symbol that represents connections, alliances, symbiosis or infinite. I attached a few symbols that could be explore, but of course you can bring differente suggestions.
• We need a clean design, nothing with too many information.

```html
<!DOCTYPE html>
<html lang="en">
<head>
<meta charset="utf-8">
<title>Lucenti Brut – Front Label</title>
<link href="https://fonts.googleapis.com/css2?family=Abril+Fatface&family=Cormorant+Garamond:wght@500&family=Montserrat:wght@400&display=swap" rel="stylesheet">
<style>
  :root {
    --page-bg: #ffffff;
    --label-cream: #f4efd3;
    --label-light: #fbf7e4;
    --label-stone: #b0ad9c;
    --ink-dark: #2e2620;
    --ink-muted: #8f8b7e;
    --teal: #00a990;
    --teal-soft: #33b8a4;
    --gold: #b8974e;
  }
  html, body {
    margin: 0;
    padding: 0;
    width: 1200px;
    height: 2206px;
    overflow: hidden;
    background: var(--page-bg);
  }
  .canvas {
    position: relative;
    width: 1200px;
    height: 2206px;
  }
  .label {
    position: absolute;
    left: 0;
    top: 610px;
    width: 1200px;
    height: 997px;
    background: linear-gradient(90deg,
      var(--label-cream) 0%,
      var(--label-light) 22%,
      #e9e5cd 52%,
      var(--label-stone) 100%);
  }
  .origin-line {
    position: absolute;
    top: 72px;
    right: 60px;
    margin: 0;
    font-family: "Montserrat", sans-serif;
    font-size: 17px;
    letter-spacing: 14px;
    color: var(--ink-muted);
    text-transform: uppercase;
  }
  .symbol-area {
    position: absolute;
    left: 61px;
    top: 292px;
    width: 790px;
    height: 380px;
  }
  .brand-name {
    position: absolute;
    right: 63px;
    top: 690px;
    margin: 0;
    font-family: "Abril Fatface", serif;
    font-weight: 400;
    font-size: 132px;
    line-height: 1;
    color: var(--ink-dark);
  }
  .wine-style {
    position: absolute;
    right: 55px;
    top: 827px;
    margin: 0;
    font-family: "Cormorant Garamond", serif;
    font-weight: 500;
    font-size: 58px;
    letter-spacing: 10px;
    line-height: 1;
    color: var(--ink-muted);
  }
</style>
</head>
<body>
  <main class="canvas">
    <section class="label">
      <p class="origin-line">Wines of Italy</p>
      <svg class="symbol-area" viewBox="0 0 790 380" role="img" aria-label="Infinity symbol in striped teal and gold, representing an embrace">
        <defs>
          <linearGradient id="symbolTone" x1="0" y1="0" x2="1" y2="0">
            <stop offset="0" stop-color="#00a990"/>
            <stop offset="0.5" stop-color="#33b8a4"/>
            <stop offset="1" stop-color="#b8974e"/>
          </linearGradient>
        </defs>
        <rect x="0" y="0" width="790" height="380" rx="60" fill="url(#symbolTone)" opacity="0.55"/>
      </svg>
      <h1 class="brand-name">Lucenti</h1>
      <p class="wine-style">BRUT</p>
    </section>
  </main>
</body>
</html>
```